Site for entrepreneurs/small businesses needs Logo, Homepage

Looking for a logo, either an icon, or stylized text, or a combination of both, and a home page design which fits with it. The logo will be for use on the public website as well as for printed collateral (business cards, post cards, brochures and various other marketing materials).

The site is called BrimTowl (BrimTowl.example). This is to be a national, and eventually an international brand. The new service will provide an easy-to-use platform for entrepreneurs to build their business and web presence together in an integrated way which allows them to focus on their core competency.

The site/service will be dead-simple to use, A/B/C, 1/2/3. We will want some sort of "Get started for FREE" promotional space to collect the person's email address with multiple points of interest which guide the user back to this one call to action: sign up for free. We will feature editorial/blog stories, customer testimonials, and present several key features the the reader just can't live without if they are starting a new business.

Criteria:
* Refer to our comparable sites/logos in the design document attached
* Incorporate our color scheme (but complementary colors welcome)
* No Serif fonts!
* No photo-realistic elements for logo
* Logo must present well in gray scale and/or black/white (for printed materials)
* Strokes/borders that are wider to promote simplicity (vs. thin/precise lines which promote technical complexity)

Inspirations:
* Creative/Custom (but legible) fonts
* Excitement, energetic, jumping for joy
* Karate / Ninja / Power / Precision
* Dance Moves
* Regional influences: California, Silicon Valley, West Coast, Surf City, Beaches, Sunset
* Simple/easy, no-brainer solutions

Target Market(s)

Small Businesses / Entrepreneurs

Logo Text

BrimTowl or BrimTowl.example

Number of Pages Required

1 page

Font styles to use
Sans Serif
Decorative

Requirements
Must have
• See the attached style guide (PDF)

```html
<!DOCTYPE html>
<html lang="en">
<head>
<meta charset="utf-8">
<title>BrimTowl — Build your business</title>
<link href="https://fonts.googleapis.com/css2?family=Montserrat:wght@400;500;600;700;800&display=swap" rel="stylesheet">
<style>
:root{
  --teal-dark:#0f3a49;
  --navy:#0c2a4a;
  --blue:#2b5a96;
  --orange:#f7931e;
  --gray-bg:#f3f3f6;
  --white:#ffffff;
  --text:#4a4f5a;
  --muted:#8a8f99;
  --ink:#1b2a3a;
}
*{box-sizing:border-box;margin:0;padding:0}
html,body{width:1200px;height:4433px;overflow:hidden}
body{position:relative;background:var(--white);font-family:'Montserrat',sans-serif;color:var(--text)}
.backdrop{position:absolute;left:0;top:0;width:1200px;height:4433px}
.abs{position:absolute}
.btn{position:absolute;display:flex;align-items:center;justify-content:center;background:var(--orange);color:var(--white);font-weight:700;border-radius:30px;text-transform:uppercase;letter-spacing:.3px}
.art{position:absolute}

/* header */
.brand{position:absolute;display:flex;align-items:center;gap:12px;color:var(--white);font-weight:700}
.brand-dot{border-radius:50%;background:var(--orange);flex:none}
.nav{position:absolute;left:676px;top:27px;display:flex;gap:30px;font-size:13px;font-weight:700;color:var(--white)}
.nav .active{color:var(--orange)}

/* hero */
.hero-title{left:135px;top:196px;font-size:38px;line-height:44px;font-weight:800;color:var(--white)}
.field{position:absolute;left:135px;width:275px;height:42px;background:#eef0f2;border-radius:6px;display:flex;align-items:center;gap:10px;padding-left:18px;font-size:13px;font-weight:500;color:#3a4350}
.hero-art{left:560px;top:120px;width:560px;height:545px;border-radius:40px;background:radial-gradient(circle at 50% 45%,#e9edf2 0,#c7d3de 45%,rgba(15,58,73,0) 72%)}

/* welcome */
.welcome-art{left:60px;top:755px;width:575px;height:455px;border-radius:30px;background:linear-gradient(135deg,#eef0fb,#c9cdf3 55%,#f6d46a)}
.welcome-label{left:830px;top:838px;font-size:16px;font-weight:700;color:var(--ink)}
.welcome-name{left:735px;top:855px;display:flex;align-items:center;gap:18px;font-size:50px;font-weight:700;color:var(--teal-dark)}
.welcome-text{left:735px;top:950px;width:360px;font-size:13px;line-height:20px}

/* section titles */
.sec-title{position:absolute;left:0;width:1200px;text-align:center;font-size:27px;font-weight:800;color:var(--navy)}
.sec-bar{position:absolute;left:570px;width:60px;height:6px;border-radius:3px;background:#d5d7dc}

/* services */
.card{position:absolute;width:222px;height:288px;background:var(--white);border-radius:8px;box-shadow:0 6px 18px rgba(20,30,50,.14);text-align:center}
.card svg{position:absolute;left:81px;top:32px}
.card h3{position:absolute;left:0;top:118px;width:100%;font-size:15px;font-weight:700;color:var(--ink)}
.card p{position:absolute;left:22px;top:160px;width:178px;font-size:11px;line-height:16px;color:var(--text)}
.card .btn{left:71px;top:245px;width:80px;height:24px;font-size:10px}

/* features */
.feat-title{left:147px;top:2363px;font-size:27px;font-weight:800;color:var(--navy)}
.feat-text{left:147px;top:2425px;width:330px;font-size:14px;line-height:21px}
.feat-list{left:147px;top:2500px;list-style:none;font-size:12px;line-height:22px}
.feat-list li{padding-left:20px;position:relative}
.feat-list li::before{content:"";position:absolute;left:2px;top:9px;width:6px;height:6px;border-radius:50%;background:var(--orange)}
.feat-art{left:517px;top:2365px;width:621px;height:458px;border-radius:50%;background:radial-gradient(ellipse at 50% 55%,#bfe3f7,#dff1fb 55%,rgba(255,255,255,0) 72%)}

/* blog */
.post{position:absolute;top:3083px;width:278px;height:390px;background:var(--white);box-shadow:0 6px 18px rgba(20,30,50,.13)}
.post .thumb{position:absolute;left:0;top:0;width:278px;height:213px}
.post h3{position:absolute;left:34px;top:228px;width:220px;font-size:15px;line-height:19px;font-weight:800;color:var(--ink);text-transform:uppercase}
.post p{position:absolute;left:34px;top:280px;width:210px;font-size:12px;line-height:16px}
.post .btn{left:34px;top:350px;width:90px;height:24px;font-size:10px}

/* testimonials */
.testi-label{left:147px;top:3680px;font-size:17px;font-weight:700;color:var(--white)}
.testi-title{left:147px;top:3708px;font-size:36px;font-weight:800;color:var(--white)}
.quote-card{left:523px;top:3683px;width:532px;height:219px;background:var(--white);border-radius:8px 60px 8px 60px}
.quote-mark{position:absolute;font-size:46px;font-weight:700;color:#c4c8cf;line-height:1}
.stars{position:absolute;left:92px;top:34px;display:flex;gap:3px}
.quote-text{position:absolute;left:94px;top:58px;width:380px;font-size:12px;line-height:17px}
.quote-name{position:absolute;left:94px;top:150px;font-size:11px;font-weight:700;color:var(--blue)}
.quote-place{position:absolute;left:94px;top:166px;font-size:10px;color:var(--muted)}
.dots{left:968px;top:3921px;display:flex;gap:8px}
.dots span{width:9px;height:9px;border-radius:50%;background:#c9d3e4}
.dots .on{background:var(--orange)}
.megaphone-art{left:355px;top:3858px;width:310px;height:177px;border-radius:50%;background:radial-gradient(ellipse,#e7edf5,#7f9abf 55%,rgba(43,90,150,0) 72%)}

/* footer */
.foot-col{position:absolute;top:4113px;color:var(--white)}
.foot-col h4{font-size:13px;font-weight:700;margin-bottom:18px}
.foot-line{display:flex;align-items:flex-start;gap:12px;font-size:12px;line-height:16px;margin-bottom:16px}
.foot-menu{font-size:12px;line-height:17px;list-style:none}
.social{display:flex;align-items:center;gap:12px;font-size:12px;margin-bottom:14px}
.social span.dot{width:26px;height:26px;border-radius:50%;background:var(--blue)}
.copyright{left:0;top:4366px;width:1200px;text-align:center;font-size:11px;color:#aab4c3}
</style>
</head>
<body>

<svg class="backdrop" viewBox="0 0 1200 4433" aria-hidden="true">
  <polygon points="0,0 1200,0 1200,470 0,710" fill="#0f3a49"/>
  <polygon points="0,1310 1200,1250 1200,2300 0,2240" fill="#f3f3f6"/>
  <polygon points="0,2850 1200,2790 1200,3530 0,3580" fill="#f3f3f6"/>
  <polygon points="0,3580 1200,3530 1200,4030 0,4070" fill="#2b5a96"/>
  <polygon points="0,4070 1200,4030 1200,4433 0,4433" fill="#0c2a4a"/>
</svg>

<!-- header -->
<header>
  <div class="brand" style="left:133px;top:36px;font-size:40px">
    <span class="brand-dot" style="width:34px;height:34px"></span>BrimTowl
  </div>
  <nav class="nav">
    <span class="active">HOME</span><span>ABOUT US</span><span>SERVICES</span><span>BLOG</span><span>CONTACT US</span>
  </nav>
</header>

<!-- hero -->
<section class="hero">
  <h1 class="abs hero-title">GET STARTED<br>FOR FREE</h1>
  <div class="field" style="top:313px">
    <svg width="14" height="12" viewBox="0 0 14 12"><rect x="1" y="1" width="12" height="10" rx="1.5" fill="none" stroke="#3a4350" stroke-width="1.8"/><path d="M1.5 2 7 7l5.5-5" fill="none" stroke="#3a4350" stroke-width="1.8"/></svg>
    E-mail id
  </div>
  <div class="field" style="top:366px">
    <svg width="12" height="13" viewBox="0 0 12 13"><circle cx="6" cy="3.5" r="3" fill="#3a4350"/><path d="M0 13c0-4 2.5-6 6-6s6 2 6 6z" fill="#3a4350"/></svg>
    Name
  </div>
  <div class="btn" style="left:135px;top:438px;width:275px;height:44px;font-size:15px">Sign up for free</div>
  <div class="art hero-art" role="img" aria-label="Illustration of a person working at a desk with a laptop, charts and a floating analytics screen"></div>
</section>

<!-- welcome -->
<section class="welcome">
  <div class="art welcome-art" role="img" aria-label="Isometric illustration of a small digital city with people working on screens and charts"></div>
  <p class="abs welcome-label">WELCOME TO</p>
  <div class="abs welcome-name"><span class="brand-dot" style="width:60px;height:60px"></span><span style="margin-top:18px">BrimTowl</span></div>
  <p class="abs welcome-text">At vero eos et accusamus et iusto odio dignissimos ducimus qui blanditiis praesentium voluptatum deleniti atque corrupti quos dolores et quas molestias excepturi sint occaecati cupiditate non provident, similique sunt in culpa qui officia deserunt mollitia.</p>
  <div class="btn" style="left:735px;top:1093px;width:135px;height:40px;font-size:12px">Read more</div>
</section>

<!-- services -->
<section class="services">
  <h2 class="sec-title" style="top:1385px">OUR SERVICES</h2>
  <div class="sec-bar" style="top:1432px"></div>

  <div class="card" style="left:133px;top:1525px">
    <svg width="60" height="60" viewBox="0 0 60 60"><circle cx="30" cy="16" r="12" fill="#0c2a4a"/><path d="M6 58c0-16 10-26 24-26s24 10 24 26z" fill="#0c2a4a"/><path d="M30 32l-4 8 4 14 4-14z" fill="#fff"/></svg>
    <h3>Entrepreneurs</h3>
    <p>At vero eos et accusamus et iusto odio dignissimos ducimus qui bla nditis praesentium.</p>
    <div class="btn">Read more</div>
  </div>
  <div class="card" style="left:372px;top:1532px">
    <svg width="60" height="60" viewBox="0 0 60 60"><rect x="2" y="18" width="14" height="24" rx="2" fill="#0c2a4a"/><rect x="44" y="18" width="14" height="24" rx="2" fill="#0c2a4a"/><path d="M16 22h12l8 4 8-4v18l-10 8-18-8z" fill="#0c2a4a"/></svg>
    <h3>Build Business</h3>
    <p>At vero eos et accusamus et iusto odio dignissimos ducimus qui bla nditis praesentium.</p>
    <div class="btn">Read more</div>
  </div>
  <div class="card" style="left:609px;top:1525px">
    <svg width="60" height="60" viewBox="0 0 60 60"><rect x="6" y="6" width="22" height="22" rx="2" fill="#0c2a4a"/><rect x="32" y="6" width="22" height="22" rx="2" fill="#0c2a4a"/><rect x="6" y="32" width="22" height="22" rx="2" fill="#0c2a4a"/><rect x="32" y="32" width="22" height="22" rx="2" fill="#0c2a4a"/><circle cx="30" cy="17" r="5" fill="#0c2a4a"/><circle cx="17" cy="30" r="5" fill="#fff"/></svg>
    <h3>Easy to Use</h3>
    <p>At vero eos et accusamus et iusto odio dignissimos ducimus qui bla nditis praesentium.</p>
    <div class="btn">Read more</div>
  </div>
  <div class="card" style="left:848px;top:1525px">
    <svg width="60" height="60" viewBox="0 0 60 60"><path d="M10 34V28a20 20 0 0 1 40 0v6" fill="none" stroke="#0c2a4a" stroke-width="5"/><rect x="6" y="30" width="12" height="18" rx="4" fill="#0c2a4a"/><rect x="42" y="30" width="12" height="18" rx="4" fill="#0c2a4a"/><path d="M48 48q0 8-14 8" fill="none" stroke="#0c2a4a" stroke-width="3"/></svg>
    <h3>Support</h3>
    <p>At vero eos et accusamus et iusto odio dignissimos ducimus qui bla nditis praesentium.</p>
    <div class="btn">Read more</div>
  </div>

  <div class="card" style="left:133px;top:1835px">
    <svg width="60" height="60" viewBox="0 0 60 60"><path d="M4 8h30a4 4 0 0 1 4 4v16a4 4 0 0 1-4 4H16l-8 8v-8H4a4 4 0 0 1-4-4V12a4 4 0 0 1 4-4z" fill="#0c2a4a"/><path d="M42 22h12a4 4 0 0 1 4 4v16a4 4 0 0 1-4 4h-2v8l-8-8H28a4 4 0 0 1-4-4v-6h14a4 4 0 0 0 4-4z" fill="#0c2a4a"/></svg>
    <h3>Customer Satisfaction</h3>
    <p>At vero eos et accusamus et iusto odio dignissimos ducimus qui bla nditis praesentium.</p>
    <div class="btn">Read more</div>
  </div>
  <div class="card" style="left:372px;top:1842px">
    <svg width="60" height="60" viewBox="0 0 60 60"><circle cx="12" cy="14" r="7" fill="#0c2a4a"/><path d="M4 58V30a6 6 0 0 1 6-6h8l10 8-3 4-9-5v27z" fill="#0c2a4a"/><rect x="26" y="6" width="30" height="24" fill="none" stroke="#0c2a4a" stroke-width="4"/><path d="M41 30v28M33 58h16" stroke="#0c2a4a" stroke-width="4"/></svg>
    <h3>Training</h3>
    <p>At vero eos et accusamus et iusto odio dignissimos ducimus qui bla nditis praesentium.</p>
    <div class="btn">Read more</div>
  </div>
  <div class="card" style="left:609px;top:1835px">
    <svg width="60" height="60" viewBox="0 0 60 60"><circle cx="24" cy="26" r="9" fill="#0c2a4a"/><path d="M6 58c0-12 8-20 18-20s18 8 18 20z" fill="#0c2a4a"/><circle cx="46" cy="12" r="10" fill="#0c2a4a"/><rect x="44.5" y="6" width="3" height="8" fill="#fff"/><rect x="44.5" y="16" width="3" height="3" fill="#fff"/></svg>
    <h3>Help Business</h3>
    <p>At vero eos et accusamus et iusto odio dignissimos ducimus qui bla nditis praesentium.</p>
    <div class="btn">Read more</div>
  </div>
  <div class="card" style="left:848px;top:1835px">
    <svg width="60" height="60" viewBox="0 0 60 60"><rect x="6" y="38" width="10" height="18" fill="#0c2a4a"/><rect x="20" y="28" width="10" height="28" fill="#0c2a4a"/><rect x="34" y="32" width="10" height="24" fill="#0c2a4a"/><rect x="48" y="18" width="10" height="38" fill="#0c2a4a"/><path d="M6 28 22 14l12 8 20-18" fill="none" stroke="#0c2a4a" stroke-width="3"/></svg>
    <h3>Successful Business</h3>
    <p>At vero eos et accusamus et iusto odio dignissimos ducimus qui bla nditis praesentium.</p>
    <div class="btn">Read more</div>
  </div>
</section>

<!-- features -->
<section class="features">
  <h2 class="abs feat-title">FEATURES</h2>
  <p class="abs feat-text">At vero eos et accusamus et iusto odio dignissimos ducimus qui blanditiis praesentium voluptatum.</p>
  <ul class="abs feat-list">
    <li>Lorem Ipsum is simply dummy text of the printing</li>
    <li>Contrary to popular belief</li>
    <li>It is a long established fact that a</li>
    <li>There are many variations of passages of Lorem</li>
    <li>Contrary to popular belief lorem</li>
    <li>Sed ut perspiciatis unde omnis</li>
  </ul>
  <div class="btn" style="left:147px;top:2688px;width:135px;height:40px;font-size:12px">Read more</div>
  <div class="art feat-art" role="img" aria-label="Isometric illustration of a team collaborating around a large video-call screen, books and tools"></div>
</section>

<!-- blog -->
<section class="blog">
  <h2 class="sec-title" style="top:2945px">LATEST BLOG</h2>
  <div class="sec-bar" style="top:2993px"></div>

  <article class="post" style="left:148px">
    <div class="thumb" role="img" aria-label="Illustration of a person surrounded by digital business icons" style="background:linear-gradient(160deg,#1d8ba3,#0f5d72)"></div>
    <h3>Lorem ipsum dolor sit sectetur adipisci</h3>
    <p>Lorem ipsum dolor sit amet, consectetur adipiscing elit, sed do eiusmod tempor</p>
    <div class="btn">Read more</div>
  </article>
  <article class="post" style="left:455px">
    <div class="thumb" role="img" aria-label="Illustration of a person on a stack of books reaching for a goal" style="background:linear-gradient(160deg,#1c6a80,#0f3a49)"></div>
    <h3>Lorem ipsum dolor sit sectetur adipisci</h3>
    <p>Lorem ipsum dolor sit amet, consectetur adipiscing elit, sed do eiusmod tempor</p>
    <div class="btn">Read more</div>
  </article>
  <article class="post" style="left:763px">
    <div class="thumb" role="img" aria-label="Illustration of business people climbing steps to a flag on a mountain" style="background:linear-gradient(180deg,#37a8e2,#bfe4f6)"></div>
    <h3>Lorem ipsum dolor sit sectetur adipisci</h3>
    <p>Lorem ipsum dolor sit amet, consectetur adipiscing elit, sed do eiusmod tempor</p>
    <div class="btn">Read more</div>
  </article>
</section>

<!-- testimonials -->
<section class="testimonials">
  <p class="abs testi-label">TESTIMONIALS</p>
  <h2 class="abs testi-title">HAPPY CLIENTS</h2>
  <div class="art megaphone-art" role="img" aria-label="Illustration of a megaphone with small floating icons"></div>
  <div class="abs quote-card">
    <span class="quote-mark" style="left:52px;top:22px">“</span>
    <div class="stars">
      <svg width="80" height="14" viewBox="0 0 80 14" fill="#2b5a96"><g id="s"><polygon points="7,0 9,5 14,5 10,8.5 11.5,14 7,10.5 2.5,14 4,8.5 0,5 5,5"/></g><use href="#s" x="16"/><use href="#s" x="32"/><use href="#s" x="48"/><use href="#s" x="64"/></svg>
    </div>
    <p class="quote-text">At vero eos et accusamus et iusto odio dignissimos ducimus qui blanditiis praesentium voluptatum deleniti atque corrupti quos dolores et quas molestias excepturi sint occaecati cupiditate non provident, similique sunt in culpa</p>
    <p class="quote-name">RICHARD</p>
    <p class="quote-place">England</p>
    <span class="quote-mark" style="left:330px;top:160px">”</span>
  </div>
  <div class="abs dots"><span></span><span></span><span class="on"></span><span></span><span></span></div>
</section>

<!-- footer -->
<footer>
  <div class="brand" style="left:133px;top:4165px;font-size:40px">
    <span class="brand-dot" style="width:34px;height:34px"></span>BrimTowl
  </div>
  <div class="foot-col" style="left:479px">
    <h4>CONTACT US</h4>
    <div class="foot-line">
      <svg width="12" height="16" viewBox="0 0 12 16"><path d="M6 0a6 6 0 0 1 6 6c0 4-6 10-6 10S0 10 0 6a6 6 0 0 1 6-6z" fill="#fff"/><circle cx="6" cy="6" r="2.2" fill="#0c2a4a"/></svg>
      <span>88 Harbor Lane<br>Seaside, CA 90000</span>
    </div>
    <div class="foot-line">
      <svg width="14" height="14" viewBox="0 0 14 14"><path d="M3 0l3 3-2 2a9 9 0 0 0 5 5l2-2 3 3-2 3C6 14 0 8 0 3z" fill="#fff"/></svg>
      <span>555.010.2200</span>
    </div>
    <div class="foot-line">
      <svg width="14" height="11" viewBox="0 0 14 11"><rect width="14" height="11" rx="1.5" fill="#fff"/><path d="M1 1.5 7 6l6-4.5" fill="none" stroke="#0c2a4a" stroke-width="1.5"/></svg>
      <span>info@brimtowl.example</span>
    </div>
  </div>
  <div class="foot-col" style="left:736px">
    <h4>MENU</h4>
    <ul class="foot-menu"><li>Home</li><li>About Us</li><li>Services</li><li>Blog</li><li>Contact Us</li></ul>
  </div>
  <div class="foot-col" style="left:940px">
    <h4>CONNECT WITH US</h4>
    <div class="social"><span class="dot"></span>Socialite</div>
    <div class="social"><span class="dot"></span>Chirper</div>
    <div class="social"><span class="dot"></span>WorkLink</div>
  </div>
  <p class="abs copyright">Copyrights @ 2018 All Rights Reserved</p>
</footer>

</body>
</html>
```